Buisness Card for an Agricultural Contracting and Earthmoving Company

We need a business card for a new business based in Kilmore, Victoria. We are a company that specialises in two areas the first is and Earthmoving company, we do large jobs such as soccer fields to small jobs such as house cuts and riding arena's, drainage, and dams. The other side of the business specialises in Agricultural improvements and hay contracting. We require a card to represent both sides of the business. Must have the following information: Dale Purvick, 2947 Tambrook Rd, Tarrowee Vale 3519, ph:03 5924 3086, mob: 0427 913 648, e-mail: dale@purvickworks.com.au. Earthmoving and Agricultural Contracting.

Target Market(s)

Builder's, Council's, new home buyers, Farmers

Industry/Entity Type

House

Font styles to use
Sans Serif

Colors
ec2026
000000
5c5c5c
ffffff

Requirements
Must have
• Both facets of the business represented. Company logo

```html
<!DOCTYPE html>
<html lang="en">
<head>
<meta charset="utf-8">
<title>Purvick Works – Business Card</title>
<link rel="stylesheet" href="https://fonts.googleapis.com/css2?family=Archivo:wght@700&family=Questrial&display=swap">
<style>
  :root {
    --red: #ec2026;
    --black: #000000;
    --grey: #5c5c5c;
    --ink: #3a3a3a;
    --white: #ffffff;
    --backdrop: #9c9d9f;
  }
  * { box-sizing: border-box; margin: 0; padding: 0; }
  html, body { width: 1200px; height: 1000px; overflow: hidden; }
  body { background: var(--backdrop); position: relative; font-family: "Questrial", sans-serif; }

  .card {
    position: absolute;
    width: 600px;
    height: 400px;
    border-radius: 30px;
    overflow: hidden;
    background: var(--black);
  }
  .card--front { left: 150px; top: 90px; }
  .card--back { left: 470px; top: 520px; }

  .brand {
    position: absolute;
    left: 0; right: 0;
    display: flex;
    align-items: center;
    justify-content: center;
    gap: 14px;
  }
  .brand__mark { width: 26px; height: 26px; background: var(--red); }
  .brand__name {
    font-family: "Archivo", sans-serif;
    font-weight: 700;
    color: var(--red);
    text-transform: uppercase;
    letter-spacing: 1px;
  }
  .card--front .brand { top: 222px; }
  .card--front .brand__name { font-size: 34px; }
  .card--back .brand { top: 138px; }
  .card--back .brand__name { font-size: 28px; }

  .tagline-band {
    position: absolute;
    left: 0; right: 0; bottom: 0;
    height: 90px;
    background: var(--red);
    display: flex;
    align-items: center;
    justify-content: center;
  }
  .tagline {
    font-family: "Archivo", sans-serif;
    font-weight: 700;
    font-size: 18px;
    color: var(--ink);
    text-transform: uppercase;
    letter-spacing: 0.3px;
  }

  .wave { position: absolute; inset: 0; }

  .holder {
    position: absolute;
    left: 78px; top: 262px;
    font-size: 20px;
    letter-spacing: 1.5px;
    text-transform: uppercase;
    color: var(--ink);
  }
  .contacts {
    position: absolute;
    left: 295px; top: 222px;
    list-style: none;
  }
  .contacts li {
    display: flex;
    align-items: center;
    gap: 6px;
    height: 23px;
    font-size: 17px;
    letter-spacing: 0.5px;
    color: var(--ink);
  }
  .contacts svg { width: 18px; height: 18px; flex: none; }
  .address {
    position: absolute;
    left: 75px; top: 340px;
    font-size: 18px;
    letter-spacing: 1px;
    color: var(--ink);
  }
</style>
</head>
<body>

  <section class="card card--front" aria-label="Business card front">
    <div class="brand">
      <span class="brand__mark"></span>
      <span class="brand__name">Purvick Works</span>
    </div>
    <div class="tagline-band">
      <p class="tagline">Earthmoving and Agricultural Contracting</p>
    </div>
  </section>

  <section class="card card--back" aria-label="Business card back">
    <svg class="wave" viewBox="0 0 600 400" preserveAspectRatio="none" aria-hidden="true">
      <path d="M0 218 C120 200 250 232 380 208 S550 160 600 155 L600 400 L0 400 Z" fill="#ec2026"/>
    </svg>
    <div class="brand">
      <span class="brand__mark"></span>
      <span class="brand__name">Purvick Works</span>
    </div>

    <p class="holder">Dale Purvick</p>

    <ul class="contacts">
      <li>
        <svg viewBox="0 0 18 18"><rect width="18" height="18" rx="2" fill="#3a3a3a"/><path d="M5 4 L7 4 L8 7 L6.8 8 C7.5 9.6 8.4 10.5 10 11.2 L11 10 L14 11 L14 13 C9 13.5 4.5 9 5 4 Z" fill="#ec2026"/></svg>
        <span>03 5924 3086</span>
      </li>
      <li>
        <svg viewBox="0 0 18 18"><rect width="18" height="18" rx="2" fill="#3a3a3a"/><rect x="6" y="3" width="6" height="12" rx="1" fill="#ec2026"/><rect x="7" y="4.5" width="4" height="7" fill="#3a3a3a"/></svg>
        <span>0427 913 648</span>
      </li>
      <li>
        <svg viewBox="0 0 18 18"><rect width="18" height="18" rx="2" fill="#3a3a3a"/><rect x="3" y="5" width="12" height="8" fill="#ec2026"/><path d="M3 5 L9 10 L15 5" fill="none" stroke="#3a3a3a" stroke-width="1.2"/></svg>
        <span>dale@purvickworks.com.au</span>
      </li>
      <li>
        <svg viewBox="0 0 18 18"><rect width="18" height="18" rx="2" fill="#3a3a3a"/><circle cx="9" cy="9" r="5.5" fill="none" stroke="#ec2026" stroke-width="1.2"/><ellipse cx="9" cy="9" rx="2.3" ry="5.5" fill="none" stroke="#ec2026" stroke-width="1"/><path d="M3.5 9 H14.5" stroke="#ec2026" stroke-width="1"/></svg>
        <span>www.purvickworks.com.au</span>
      </li>
    </ul>

    <p class="address">2947 Tambrook Rd, Tarrowee Vale 3519</p>
  </section>

</body>
</html>
```